Business Card For Video Production Company

Please NOTE: I've added some info to the must haves that I should have included at the start. Thank you.

I need a business card design for my video production company based in Orlando called Caldera Film Works. Our work consists of web video marketing (web videos), training videos, sales videos, conference and seminar video production...basically a lot of corporate based work.

We work with successful small businesses, not-for-profits and some Fortune 500 type groups. We bring a lot of knowledge, experience and attention to detail to every project.

I'd like something that communicates strength, confidence, integrity, as well as creative vision. I want to stay away from the standard icons of the media and film industry. I'd like to emphasize the colors of my logo, and also the colors of my website which has a white background. Simple is good.

Our budgets are moderate...generally $1500 to $5000.

www.calderafilm.tv

PS...We don't do weddings or recitals, or that type of production.
Updates

I want to thank all the designers for your updates. There's way too many to be able to give feedback on for all. I hope you understand that. But wow…there are so many great designs everyone has offered. I can't thank you enough…each and everyone. I hope to make my decision soon. I'm not accepting anymore designs from new designers. Brent-

Target Market(s)

Successful small businesses, marketing directors, corporate communication directors, training and human resources professionals. forward thinking not-for profits. Since my company is based in Central Florida, most of my work comes from this area too.

Industry/Entity Type

Marketing

Requirements
Must have
• website address, www.calderafilm.tv
phone number, 407-552-9031
email address, brent@calderafilm.tv

Title
Brent Caldera
Owner/Creative Director

I'd like to have a single line that goes across illustrating our services, maybe separated with bullet points:

Marketing Videos, Corporate Videos, Conference & Seminar Video Production
Should not have
• No film or video icons.
No need to pull language or copy from my website.

```html
<!DOCTYPE html>
<html lang="en">
<head>
<meta charset="utf-8">
<title>Caldera Film Works — Business Cards</title>
<link rel="stylesheet" href="https://fonts.googleapis.com/css2?family=Montserrat:wght@700&family=Questrial&family=Oswald:wght@400;500&display=swap">
<style>
  :root {
    --blue: #2a8fd9;
    --sky: #8dd0f6;
    --white: #ffffff;
    --ink: #4a4a4a;
    --muted: #8a8a8a;
    --page: #eef0f2;
  }
  * { box-sizing: border-box; margin: 0; padding: 0; }
  html, body { width: 1200px; height: 874px; overflow: hidden; }
  body { background: var(--page); position: relative; font-family: "Questrial", sans-serif; }

  .card {
    position: absolute; top: 282px; width: 540px; height: 310px;
    overflow: hidden; box-shadow: 0 6px 18px rgba(0,0,0,.14);
  }
  .card--front { left: 40px; background: var(--blue); color: var(--white); }
  .card--back  { left: 620px; background: var(--white); color: var(--ink); }

  .holder { position: absolute; left: 40px; top: 26px; font-family: "Oswald", sans-serif; letter-spacing: .08em; text-transform: uppercase; line-height: 1.25; }
  .holder__name { font-size: 13px; font-weight: 500; }
  .holder__title { font-size: 12px; }
  .card--back .holder__title { color: var(--muted); }

  .brand { position: absolute; left: 40px; top: 78px; display: flex; align-items: center; gap: 16px; }
  .brand__mark { width: 64px; height: 64px; background: var(--white); }
  .card--back .brand__mark { background: var(--sky); }
  .brand__name { font-family: "Montserrat", sans-serif; font-weight: 700; font-size: 30px; letter-spacing: -.01em; }

  .contact { position: absolute; right: 28px; top: 28px; list-style: none; font-family: "Oswald", sans-serif; font-size: 11px; letter-spacing: .07em; text-transform: uppercase; line-height: 1.6; }
  .contact li { display: flex; align-items: center; gap: 6px; }
  .contact svg { width: 10px; height: 10px; fill: currentColor; }

  .services { position: absolute; left: 0; right: 0; top: 176px; height: 84px; }
  .services svg { position: absolute; inset: 0; width: 100%; height: 100%; }
  .services__text { position: absolute; left: 58px; top: 14px; font-size: 22px; line-height: 1.3; }
  .card--front .services__text { color: var(--blue); }
  .card--back .services__text { color: var(--white); }
</style>
</head>
<body>

<section class="card card--front" aria-label="Business card front">
  <div class="holder">
    <p class="holder__name">Brent Caldera</p>
    <p class="holder__title">Owner · Creative Director</p>
  </div>
  <div class="brand">
    <span class="brand__mark"></span>
    <span class="brand__name">Caldera Film Works</span>
  </div>
  <ul class="contact">
    <li><svg viewBox="0 0 10 10"><circle cx="5" cy="5" r="4.5"/></svg>www.calderafilm.tv</li>
    <li><svg viewBox="0 0 10 10"><path d="M0 2h10v6H0z"/></svg>brent@calderafilm.tv</li>
    <li><svg viewBox="0 0 10 10"><path d="M2 0h3l1 3-2 1c1 1.5 1 2 2 2l1-2 3 1v3c-5 0-8-3-8-8z"/></svg>407-552-9031</li>
  </ul>
  <div class="services">
    <svg viewBox="0 0 540 84" preserveAspectRatio="none"><path d="M0 10h22V0h518v84H22V30H0z" fill="var(--sky)"/></svg>
    <p class="services__text">Marketing Videos · Corporate Videos<br>· Conference &amp; Seminar Video Production</p>
  </div>
</section>

<section class="card card--back" aria-label="Business card back">
  <div class="holder">
    <p class="holder__name">Brent Caldera</p>
    <p class="holder__title">Owner · Creative Director</p>
  </div>
  <div class="brand">
    <span class="brand__mark"></span>
    <span class="brand__name">Caldera Film Works</span>
  </div>
  <ul class="contact">
    <li><svg viewBox="0 0 10 10"><circle cx="5" cy="5" r="4.5"/></svg>www.calderafilm.tv</li>
    <li><svg viewBox="0 0 10 10"><path d="M0 2h10v6H0z"/></svg>brent@calderafilm.tv</li>
    <li><svg viewBox="0 0 10 10"><path d="M2 0h3l1 3-2 1c1 1.5 1 2 2 2l1-2 3 1v3c-5 0-8-3-8-8z"/></svg>407-552-9031</li>
  </ul>
  <div class="services">
    <svg viewBox="0 0 540 84" preserveAspectRatio="none"><path d="M0 10h22V0h518v84H22V30H0z" fill="var(--blue)"/></svg>
    <p class="services__text">Marketing Videos · Corporate Videos<br>· Conference &amp; Seminar Video Production</p>
  </div>
</section>

</body>
</html>
```